Letterhead - Quarrington Law Group

I receive a fantastic logo from you guys and I'd like to incorporate it into business cards and letterhead. I accidentally approved design No. 32361474 and contacted designer Ravindra, and Ravindra sent me the zip folder for Design No. 32361417, which I very much appreciate.
I'd like to order business cards and letterhead with Design No. 32361417 as soon as possible, but I want to make sure that you incorporate the correct design (attached). I'd also like to provide my information to add (address, phone number, email, fax) but I'm not quite sure how to do it.
The information that I would like on the business cards and letterhead is as follows:
Quarrington Law Group
Theodore K. Quarrington, Esq.
2741 Hollis Avenue, Suite 520
San Francisco, CA 94087
Office: (415) 378-6130
Fax: (415) 746-0183
ted@quarringtonlawgroup-example.com
Thanks in advance for any guidance.
Ted Quarrington
Quarrington Law Group
(415) 831-4497 (cell)

```html
<!DOCTYPE html>
<html lang="en">
<head>
<meta charset="utf-8">
<title>Quarrington Law Group – Letterhead</title>
<link rel="stylesheet" href="https://fonts.googleapis.com/css2?family=Arimo:wght@400;700&display=swap">
<style>
  :root {
    --brand-blue: #1b8dcc;
    --ink: #231f20;
    --body-ink: #2b2b2b;
    --paper: #ffffff;
    --backdrop: #e9e9eb;
    --signature-tint: #d6ebf7;
  }
  * { box-sizing: border-box; margin: 0; padding: 0; }
  html, body { width: 1200px; height: 874px; overflow: hidden; }
  body {
    background: var(--backdrop);
    font-family: "Arimo", Arial, sans-serif;
    position: relative;
  }
  .letterhead {
    position: absolute;
    left: 310px; top: 27px;
    width: 580px; height: 820px;
    background: var(--paper);
    overflow: hidden;
    box-shadow: 0 2px 10px rgba(0,0,0,.12);
  }
  .corner-accent { position: absolute; top: 0; right: 0; }
  .brand {
    position: absolute; left: 48px; top: 128px;
    display: flex; align-items: center; gap: 10px;
  }
  .brand-square { width: 14px; height: 14px; background: var(--brand-blue); }
  .brand-name {
    font-size: 20px; font-weight: 700; color: var(--ink);
    letter-spacing: .3px;
  }
  .letter-body {
    position: absolute; left: 82px; top: 268px; width: 420px;
    font-size: 8.6px; line-height: 1.5; color: var(--body-ink);
  }
  .letter-body p { margin-bottom: 11px; }
  .salutation { margin-bottom: 9px !important; }
  .closing { margin-top: 14px; }
  .signature {
    display: block; margin-top: 6px; width: 150px; height: 36px;
    background: linear-gradient(90deg, var(--signature-tint), #eef6fb);
    border-radius: 3px;
  }
  .contact-band {
    position: absolute; left: 0; bottom: 0; width: 100%; height: 107px;
    background: var(--brand-blue); color: #fff;
    display: grid; grid-template-columns: 112px 1px 188px 1px 1fr;
    column-gap: 12px; align-items: center;
    padding: 0 14px 0 28px;
  }
  .divider { width: 1px; height: 46px; background: rgba(255,255,255,.85); }
  .sender-name { font-size: 13px; font-weight: 700; margin-bottom: 3px; white-space: nowrap; }
  .contact-band .line { font-size: 8.5px; line-height: 1.6; display: flex; align-items: center; gap: 4px; white-space: nowrap; }
  .contact-band svg { width: 8px; height: 8px; flex: none; fill: #fff; }
  .office-address { font-style: normal; min-width: 0; }
  .office-firm { font-weight: 700; }
</style>
</head>
<body>
  <main class="letterhead">
    <svg class="corner-accent" width="186" height="131" viewBox="0 0 186 131" aria-hidden="true">
      <path d="M0 0 H186 V131 C166 80 90 18 0 0 Z" fill="var(--brand-blue)"/>
    </svg>

    <header class="brand">
      <span class="brand-square"></span>
      <span class="brand-name">Quarrington Law Group</span>
    </header>

    <section class="letter-body">
      <p class="salutation">Dear Sir,</p>
      <p>Lorem ipsum dolor sit amet, consectetur adipiscing elit, sed do eiusmod tempor incididunt ut labore et dolore magna aliqua. Ut enim ad minim veniam, quis nostrud exercitation ullamco laboris nisi ut aliquip ex ea commodo consequat. Duis aute irure dolor in reprehenderit in voluptate velit esse cillum dolore eu fugiat nulla pariatur. Excepteur sint occaecat cupidatat non proident, sunt in culpa qui officia deserunt mollit anim id est laborum. It is a long established fact that a reader will be distracted by the readable content of a page when looking at its layout. The point of using Lorem Ipsum is that it has a more-or-less normal distribution of letters, as opposed to using ‘Content here, content here’, making it look like readable English.</p>
      <p>But I must explain to you how all this mistaken idea of denouncing pleasure and praising pain was born and I will give you a complete account of the system, and expound the actual teachings of the great explorer of the truth, the master-builder of human happiness. No one rejects, dislikes, or avoids pleasure itself, because it is pleasure, but because those who do not know how to pursue pleasure rationally encounter consequences that are extremely painful. Nor again is there anyone who loves or pursues or desires to obtain pain of itself, because it is pain, but because occasionally circumstances occur in which toil and pain can procure him some great pleasure.</p>
      <p>There are many variations of passages of Lorem Ipsum available, but the majority have suffered alteration in some form, by injected humour, or randomised words which don't look even slightly believable. If you are going to use a passage of Lorem Ipsum, you need to be sure there isn't anything embarrassing hidden in the middle of text. All the Lorem Ipsum generators on the Internet tend to repeat predefined chunks as necessary, making this the first true generator on the Internet.</p>
      <p class="closing">Best Regards</p>
      <span class="signature" role="img" aria-label="Handwritten signature of Martin Hale in blue ink"></span>
    </section>

    <footer class="contact-band">
      <div class="sender">
        <div class="sender-name">Ted Quarrington</div>
        <div class="line">Quarrington Law Group</div>
        <div class="line"><svg viewBox="0 0 10 10"><path d="M2 0.5 L3.6 2.6 L2.7 3.6 Q4 6 6.4 7.3 L7.4 6.4 L9.5 8 L8.3 9.5 Q2.5 8.5 0.5 1.7 Z"/></svg>(415) 831-4497 (cell)</div>
      </div>
      <span class="divider"></span>
      <div class="office-contacts">
        <div class="line"><svg viewBox="0 0 10 10"><path d="M2 0.5 L3.6 2.6 L2.7 3.6 Q4 6 6.4 7.3 L7.4 6.4 L9.5 8 L8.3 9.5 Q2.5 8.5 0.5 1.7 Z"/></svg>(415) 378-6130</div>
        <div class="line"><svg viewBox="0 0 10 10"><path d="M2.5 0.5 H7.5 V3 H2.5 Z M0.5 3.5 H9.5 V8 H7.5 V9.5 H2.5 V8 H0.5 Z"/></svg>(415) 746-0183</div>
        <div class="line"><svg viewBox="0 0 10 10"><path d="M0.5 2 H9.5 V8.5 H0.5 Z M1 2.4 L5 5.6 L9 2.4" stroke="var(--brand-blue)" stroke-width=".8"/></svg>ted@quarringtonlawgroup-example.com</div>
        <div class="line"><svg viewBox="0 0 10 10"><circle cx="5" cy="5" r="4.5"/><path d="M0.5 5 H9.5 M5 0.5 Q2 5 5 9.5 M5 0.5 Q8 5 5 9.5" stroke="var(--brand-blue)" stroke-width=".7" fill="none"/></svg>www.quarringtonlawgroup-example.com</div>
      </div>
      <span class="divider"></span>
      <address class="office-address">
        <div class="line office-firm">Quarrington Law Group</div>
        <div class="line">Theodore K. Quarrington, Esq.</div>
        <div class="line">2741 Hollis Avenue, Suite 520</div>
        <div class="line">San Francisco, CA 94087</div>
      </address>
    </footer>
  </main>
</body>
</html>
```